Criação de Papelaria (6 itens) para Decoração & Casalto
A empresa queria:
" É um comércio de móveis planejados e móveis complementares, como sofás, cadeiras, banquetas e mesas. "

```html
<!DOCTYPE html>
<html lang="pt-BR">
<head>
<meta charset="utf-8">
<title>Casalto — Cartão de visita</title>
<link href="https://fonts.googleapis.com/css2?family=Montserrat:wght@400;500;600;700&display=swap" rel="stylesheet">
<style>
  :root {
    --bg: #e9e6e2;
    --graphite: #5b5c5f;
    --graphite-dark: #47484b;
    --wine: #8c1f26;
    --paper: #ffffff;
    --ink: #4a4a4d;
    --ink-soft: #7a7a7e;
  }
  * { margin: 0; padding: 0; box-sizing: border-box; }
  html, body { width: 1200px; height: 1200px; overflow: hidden; }
  body {
    background: var(--bg);
    font-family: "Montserrat", sans-serif;
    display: flex;
    flex-direction: column;
    align-items: center;
    justify-content: center;
    gap: 80px;
  }
  .card {
    position: relative;
    width: 770px;
    height: 440px;
    border-radius: 34px;
    overflow: hidden;
    box-shadow: 0 10px 30px rgba(0,0,0,0.12);
  }

  /* Front */
  .card--front {
    background: linear-gradient(160deg, var(--graphite) 0%, var(--graphite-dark) 100%);
  }
  .card--front .swoosh {
    position: absolute; inset: 0; width: 100%; height: 100%;
  }
  .brand {
    position: absolute;
    font-weight: 600;
    line-height: 1;
    white-space: nowrap;
  }
  .card--front .brand {
    left: 50%; top: 50%;
    transform: translate(-50%, -50%);
    color: var(--paper);
    font-size: 84px;
  }

  /* Back */
  .card--back { background: var(--paper); }
  .company {
    position: absolute; left: 70px; top: 70px;
    color: var(--wine);
    font-weight: 600;
    font-size: 17px;
    line-height: 1.35;
    text-transform: uppercase;
    letter-spacing: 0.5px;
  }
  .contacts {
    position: absolute; left: 70px; top: 170px;
    list-style: none;
    display: flex; flex-direction: column; gap: 18px;
  }
  .contact {
    display: flex; align-items: center; gap: 16px;
    color: var(--ink);
    font-size: 14px;
    font-weight: 500;
    text-transform: uppercase;
    letter-spacing: 0.4px;
  }
  .contact__icon {
    width: 28px; height: 28px; flex: none;
    border-radius: 50%;
    background: var(--graphite);
    display: flex; align-items: center; justify-content: center;
  }
  .contact__icon svg { width: 16px; height: 16px; }
  .contact__text--small { font-size: 11px; line-height: 1.4; color: var(--ink-soft); }
  .card--back .brand {
    right: 60px; top: 50%;
    transform: translateY(-50%);
    color: var(--ink);
    font-size: 48px;
  }
</style>
</head>
<body>

  <section class="card card--front" aria-label="Frente do cartão">
    <svg class="swoosh" viewBox="0 0 770 440" preserveAspectRatio="none" aria-hidden="true">
      <path d="M640 0 C720 120 735 300 690 440 L770 440 L770 0 Z" fill="#8c1f26"/>
      <path d="M655 0 C735 120 750 300 705 440 L770 440 L770 0 Z" fill="#5b5c5f"/>
    </svg>
    <p class="brand">Casalto</p>
  </section>

  <section class="card card--back" aria-label="Verso do cartão">
    <p class="company">Casalto Comércio<br>Varejista de Móveis Ltda</p>
    <ul class="contacts">
      <li class="contact">
        <span class="contact__icon"><svg viewBox="0 0 24 24"><path fill="#fff" d="M6.6 10.8a15.1 15.1 0 0 0 6.6 6.6l2.2-2.2c.3-.3.7-.4 1-.2 1.1.4 2.3.6 3.6.6.6 0 1 .4 1 1V20c0 .6-.4 1-1 1A17 17 0 0 1 3 4c0-.6.4-1 1-1h3.5c.6 0 1 .4 1 1 0 1.3.2 2.5.6 3.6.1.3 0 .7-.2 1z"/></svg></span>
        <span class="contact__text">31 3555-0142</span>
      </li>
      <li class="contact">
        <span class="contact__icon"><svg viewBox="0 0 24 24" fill="none" stroke="#fff" stroke-width="2"><circle cx="12" cy="12" r="9"/><path d="M3 12h18M12 3c3 3 3 15 0 18M12 3c-3 3-3 15 0 18"/></svg></span>
        <span class="contact__text">www.casalto.com.br</span>
      </li>
      <li class="contact">
        <span class="contact__icon"><svg viewBox="0 0 24 24"><path fill="#fff" d="M12 2a7 7 0 0 0-7 7c0 5 7 13 7 13s7-8 7-13a7 7 0 0 0-7-7zm0 9.5A2.5 2.5 0 1 1 12 6.5a2.5 2.5 0 0 1 0 5z"/></svg></span>
        <span class="contact__text contact__text--small">Rua das Acácias, 120, Sala 4, CEP 30100-000<br>Centro, Belo Horizonte, MG</span>
      </li>
      <li class="contact">
        <span class="contact__icon"></span>
        <span class="contact__text">casaltomoveis</span>
      </li>
      <li class="contact">
        <span class="contact__icon"></span>
        <span class="contact__text">@casaltomoveis</span>
      </li>
    </ul>
    <p class="brand">Casalto</p>
  </section>

</body>
</html>
```